Design some Business Cards for Kalvinora

Design some business Cards for my company.

Artwork is included and a sample old business card with the necessary info we must have.
We would like a new more modern look (simple, yet elegant) using our existing logo.

```html
<!DOCTYPE html>
<html lang="es">
<head>
<meta charset="utf-8">
<title>Kalvinora – Tarjetas de presentación</title>
<link href="https://fonts.googleapis.com/css2?family=Montserrat:wght@400;500;600;700&family=Lato:wght@400;700&display=swap" rel="stylesheet">
<style>
  :root {
    --bg: #3b3b3b;
    --card: #f7f7f5;
    --ink: #2b2b2b;
    --muted: #4a4a4a;
    --brand: #e8a21c;
    --rule: #d4d4d4;
  }
  * { margin: 0; padding: 0; box-sizing: border-box; }
  html, body { width: 1200px; height: 749px; overflow: hidden; }
  body { background: var(--bg); font-family: "Montserrat", sans-serif; color: var(--ink); position: relative; }

  .card {
    position: absolute;
    width: 540px; height: 300px;
    background: var(--card);
    overflow: hidden;
  }
  .card--front { left: 90px; top: 70px; }
  .card--back { left: 570px; top: 390px; }

  .wordmark {
    display: flex; align-items: center; justify-content: center; gap: 10px;
    font-family: "Montserrat", sans-serif; font-weight: 700;
    color: var(--brand); letter-spacing: 1px;
  }
  .wordmark__mark { background: var(--brand); }

  .card--front .wordmark { margin-top: 110px; font-size: 38px; }
  .card--front .wordmark__mark { width: 22px; height: 22px; }
  .front__url {
    text-align: center; margin-top: 14px;
    font-size: 19px; font-weight: 500; color: var(--ink); letter-spacing: 0.5px;
  }

  .back__band-top {
    position: absolute; top: 0; left: 190px; right: 0; height: 6px; background: var(--brand);
  }
  .back__band-bottom {
    position: absolute; bottom: 0; left: 0; right: 0; height: 10px; background: var(--brand);
  }
  .card--back .wordmark { position: absolute; top: 52px; left: 0; right: 0; font-size: 26px; }
  .card--back .wordmark__mark { width: 16px; height: 16px; }
  .back__divider {
    position: absolute; left: 270px; top: 100px; bottom: 30px; width: 1px; background: var(--rule);
  }

  .contact { position: absolute; font-family: "Lato", sans-serif; font-size: 11.5px; color: var(--muted); }
  .contact__row { display: flex; align-items: flex-start; gap: 8px; line-height: 1.35; }
  .contact__row + .contact__row { margin-top: 6px; }
  .contact__icon { width: 12px; height: 12px; flex: none; margin-top: 1px; fill: var(--ink); }

  .contact--left { left: 30px; top: 150px; }
  .contact--right { left: 300px; top: 205px; }

  .person { position: absolute; left: 300px; top: 138px; }
  .person__name { font-size: 20px; font-weight: 700; color: var(--ink); }
  .person__surname { color: var(--brand); }
  .person__role { font-size: 15px; font-weight: 400; color: var(--muted); margin-top: 2px; padding-left: 22px; }
</style>
</head>
<body>

<section class="card card--front" aria-label="Anverso de la tarjeta">
  <div class="wordmark"><span class="wordmark__mark"></span><span>KALVINORA</span></div>
  <p class="front__url">www.kalvinora.com.pa</p>
</section>

<section class="card card--back" aria-label="Reverso de la tarjeta">
  <div class="back__band-top"></div>
  <div class="wordmark"><span class="wordmark__mark"></span><span>KALVINORA</span></div>
  <div class="back__divider"></div>

  <div class="contact contact--left">
    <div class="contact__row">
      <svg class="contact__icon" viewBox="0 0 12 12"><path d="M6 0a4 4 0 0 0-4 4c0 3 4 8 4 8s4-5 4-8a4 4 0 0 0-4-4zm0 5.5A1.5 1.5 0 1 1 6 2.5a1.5 1.5 0 0 1 0 3z"/></svg>
      <span>P.H. Costa 218, Oficina 7B<br>Vía Central, junto al Parque Lineal<br>Ciudad de Panamá, Panamá</span>
    </div>
    <div class="contact__row">
      <svg class="contact__icon" viewBox="0 0 12 12"><path d="M1 4c0-2 10-2 10 0v1H8V4H4v1H1zM2 6h8l1 5H1z"/></svg>
      <span>507 555 0142</span>
    </div>
    <div class="contact__row">
      <svg class="contact__icon" viewBox="0 0 12 12"><path d="M2 0h6v4h2v8H2zM3 1v3h4V1zm1 5v1h1V6zm2 0v1h1V6zm-2 2v1h1V8zm2 0v1h1V8z"/></svg>
      <span>507 555 0187</span>
    </div>
    <div class="contact__row">
      <svg class="contact__icon" viewBox="0 0 12 12"><path d="M3 0h6v12H3zm1 1v8h4V1zm2 9a.6.6 0 1 0 0 1.2A.6.6 0 0 0 6 10z"/></svg>
      <span>507 6555 0193</span>
    </div>
  </div>

  <div class="person">
    <p class="person__name">Rodrigo T. <span class="person__surname">Salcedo</span></p>
    <p class="person__role">Vicepresidente</p>
  </div>

  <div class="contact contact--right">
    <div class="contact__row">
      <svg class="contact__icon" viewBox="0 0 12 12"><path d="M0 2h12v8H0zm1 1v.3l5 3.5 5-3.5V3zm0 1.5V9h10V4.5L6 8z"/></svg>
      <span>rodrigo@kalvinora.com.pa</span>
    </div>
    <div class="contact__row">
      <svg class="contact__icon" viewBox="0 0 12 12"><path d="M2 2h8v6H2zm1 1v4h6V3zM0 9h12v1H0z"/></svg>
      <span>www.kalvinora.com.pa</span>
    </div>
  </div>

  <div class="back__band-bottom"></div>
</section>

</body>
</html>
```